12" Touchscreen Interface Graphic Design

We have a touchscreen control system already designed with rudimentary graphics. The functionality is there, we need to make the graphics look more professional.
The new graphics design is to be 'modular' so that things can be moved within the touchscreen software.
By modular i mean that i need to for example add or remove pumps from the system, change the piping layout, move location of the various graphical elements.
I have enough graphics skills to be able to re-size, stretch, colorize the submitted design to adapt it specifically to the ongoing changing needs of the interface.
I can "cut up" the submitted design to make my individual graphical elements (for example 80x100px image for the pump) that i can then move around where i want for future systems that have different hardware configurations.
Attached are screenshots of how the interface looks at the moment, with some comments on the side.
The graphical elements need ideally to have the same pixel dimensions as on the screenshot. If changes are recommended for a specific reason, each element within the overall display should have dimensions in increments of 10px
Also attached is a screenshot from one of our other unrelated control systems that has a graphics style we would like to be close to.
Look and feel
Each slider illustrates characteristics of the customer's brand and the style your logo design should communicate.

```html
<!DOCTYPE html>
<html lang="en">
<head>
<meta charset="utf-8">
<title>Chiller Plant Control</title>
<link href="https://fonts.googleapis.com/css2?family=Poppins:wght@400;500;600&display=swap" rel="stylesheet">
<style>
  :root{
    --bg-top:#1a1d29;
    --bg-bottom:#0b0c12;
    --panel:#141826;
    --panel-edge:#3b4254;
    --readout:#050608;
    --readout-edge:#4a4f5c;
    --text:#ffffff;
    --blue-hi:#47a6ff;
    --blue-lo:#0a5fe0;
    --green-hi:#4fd12a;
    --green-lo:#15301a;
    --grey-hi:#8a8a8a;
    --grey-lo:#4a4a4a;
    --cyan:#2fd9e6;
    --cyan-hi:#b7f6fb;
    --yellow:#ecea2a;
    --yellow-hi:#fffcb0;
    --valve-green:#5cc21f;
    --valve-red:#b3140f;
  }
  *{box-sizing:border-box;margin:0;padding:0}
  html,body{width:1200px;height:736px;overflow:hidden;background:var(--bg-bottom)}
  body{font-family:"Poppins",sans-serif;color:var(--text)}
  .stage{position:relative;width:1250px;height:767px;transform:scale(.96);transform-origin:0 0;
    background:linear-gradient(180deg,var(--bg-top),var(--bg-bottom))}
  .pipes{position:absolute;left:0;top:0}
  .abs{position:absolute}

  .btn{position:absolute;display:flex;align-items:center;justify-content:center;text-align:center;
    background:linear-gradient(180deg,var(--blue-hi),var(--blue-lo));font-size:12px;line-height:1.3;
    text-transform:uppercase;border-radius:2px}
  .btn-grey{background:linear-gradient(180deg,var(--grey-hi),var(--grey-lo));border:2px solid #9a9a9a;
    font-size:19px;line-height:1.3}
  .readout{position:absolute;display:flex;align-items:center;justify-content:center;background:var(--readout);
    border:1px solid var(--readout-edge);border-radius:4px;font-size:13px}
  .readout-lg{font-size:19px}
  .readout-target{flex-direction:column;font-size:12px;line-height:1.2}
  .mode-display{font-size:19px}
  .pump{position:absolute;border-radius:8px}
  .pump-sea-duty{background:linear-gradient(90deg,#a84a4a,#e88d8a,#9c3f3f)}
  .pump-sea-standby{background:linear-gradient(90deg,#2f5f8c,#8cb7de,#2b5a86)}
  .pump-circ-duty{background:linear-gradient(90deg,#2f8a45,#8fe0a0,#2b7f40)}
  .pump-circ-standby{background:linear-gradient(90deg,#a86a2c,#f0b878,#9c5f25)}
  .pump-label{position:absolute;font-size:19px;transform:translateX(-50%);white-space:nowrap}

  .chiller{position:absolute;width:155px;height:196px;background:var(--panel);border:1px solid var(--panel-edge);
    border-radius:8px;overflow:hidden;display:flex;flex-direction:column}
  .chiller-temps{height:33px;display:flex;justify-content:space-between;align-items:center;padding:0 5px}
  .chiller-temps .value{width:66px;height:26px;background:var(--readout);border-radius:4px;font-size:16px;
    display:flex;align-items:center;justify-content:center}
  .chiller-alarms{height:45px;background:linear-gradient(180deg,var(--green-hi) 0%,#2b6a22 45%,var(--panel) 100%);
    font-size:12px;padding:2px 5px}
  .alarm-row{height:21px;display:flex;align-items:center}
  .alarm-row .box{background:var(--readout);border-radius:3px;height:18px;display:flex;align-items:center;
    justify-content:flex-end;padding-right:5px}
  .alarm-count{width:50px}
  .alarm-tag{width:34px;padding-left:4px}
  .pressure{width:34px}
  .unit{padding-left:4px}
  .spacer{width:50px}
  .freeze-stop{height:23px;display:flex;align-items:center;justify-content:center;font-size:12px;font-weight:600}
  .inhibit-toggle{height:46px;background:linear-gradient(180deg,var(--blue-hi),var(--blue-lo));display:flex;
    flex-direction:column;justify-content:space-around;align-items:center;font-size:12px;padding:2px 0}
  .chiller-name{height:25px;margin-top:2px;background:linear-gradient(180deg,var(--green-hi),var(--green-lo));
    display:flex;align-items:center;justify-content:center;font-size:12px}
  .run-hours{flex:1;display:flex;align-items:center;justify-content:center;font-size:13px;gap:8px;padding-bottom:2px}
  .run-hours .box{background:var(--readout);border-radius:3px;padding:0 8px;height:20px;display:flex;align-items:center}
</style>
</head>
<body>
<div class="stage">
  <svg class="pipes" width="1250" height="767" viewBox="0 0 1250 767">
    <g fill="none" stroke-linecap="round" stroke-linejoin="round">
      <g stroke="var(--cyan)" stroke-width="7">
        <path d="M0 46 H985 Q995 46 995 56 V104"/>
        <path d="M563 46 V104 M778 46 V104"/>
        <path d="M485 46 V368 Q485 378 495 378 H985 Q995 378 995 388 V436"/>
        <path d="M563 378 V436 M778 378 V436"/>
      </g>
      <g stroke="var(--cyan-hi)" stroke-width="1.5" opacity=".7">
        <path d="M0 45 H985 Q994 45 994 56 V104"/>
        <path d="M484 46 V368 Q484 377 495 377 H985 Q994 377 994 388 V436"/>
      </g>
      <g stroke="var(--yellow)" stroke-width="7">
        <path d="M640 100 V88 Q640 78 650 78 H1195 Q1205 78 1205 88 V672 Q1205 682 1195 682 H232"/>
        <path d="M855 78 V100 M1070 78 V100"/>
        <path d="M640 432 V420 Q640 410 650 410 H1205"/>
        <path d="M855 410 V432 M1070 410 V432"/>
        <path d="M232 278 V172 Q232 162 222 162 H85 Q75 162 75 172 V268 Q75 278 85 278 H430"/>
        <path d="M408 278 V542 Q408 552 418 552 H432"/>
        <path d="M232 682 V572 Q232 562 222 562 H85 Q75 562 75 572 V672 Q75 682 85 682 H232"/>
      </g>
      <g stroke="var(--yellow-hi)" stroke-width="1.5" opacity=".7">
        <path d="M650 77 H1195 Q1204 77 1204 88 V672"/>
        <path d="M232 681 H1195"/>
        <path d="M232 277 H430"/>
      </g>
    </g>
    <g fill="var(--cyan)">
      <polygon points="403,46 425,32 425,60"/>
      <polygon points="563,102 548,125 578,125"/>
      <polygon points="778,102 763,125 793,125"/>
      <polygon points="995,102 980,125 1010,125"/>
      <polygon points="563,434 548,457 578,457"/>
      <polygon points="778,434 763,457 793,457"/>
      <polygon points="995,434 980,457 1010,457"/>
    </g>
    <g fill="var(--yellow)">
      <polygon points="624,100 656,100 640,122"/>
      <polygon points="839,100 871,100 855,122"/>
      <polygon points="1054,100 1086,100 1070,122"/>
      <polygon points="624,432 656,432 640,454"/>
      <polygon points="839,432 871,432 855,454"/>
      <polygon points="1054,432 1086,432 1070,454"/>
      <polygon points="432,262 455,278 432,294"/>
      <polygon points="432,536 455,552 432,568"/>
      <polygon points="408,665 430,682 408,699"/>
    </g>
    <g class="valve">
      <rect x="1142" y="66" width="6" height="12" fill="var(--yellow)"/>
      <circle cx="1145" cy="46" r="20" fill="var(--valve-green)" stroke="var(--yellow)" stroke-width="3"/>
      <polygon points="1134,46 1152,35 1152,57" fill="var(--yellow)"/>
      <rect x="1142" y="398" width="6" height="12" fill="var(--yellow)"/>
      <circle cx="1145" cy="378" r="20" fill="var(--valve-red)" stroke="var(--yellow)" stroke-width="3"/>
      <polygon points="1134,378 1152,367 1152,389" fill="var(--yellow)"/>
    </g>
  </svg>

  <div class="pump pump-sea-duty" style="left:122px;top:95px;width:62px;height:85px" role="img" aria-label="Sea water duty pump"></div>
  <div class="pump pump-sea-standby" style="left:118px;top:210px;width:68px;height:90px" role="img" aria-label="Sea water standby pump"></div>
  <div class="pump pump-circ-duty" style="left:118px;top:495px;width:68px;height:85px" role="img" aria-label="Circulation duty pump"></div>
  <div class="pump pump-circ-standby" style="left:116px;top:612px;width:70px;height:88px" role="img" aria-label="Circulation standby pump"></div>
  <div class="pump-label" style="left:152px;top:183px">SEA WATER</div>
  <div class="pump-label" style="left:156px;top:583px">CIRCULATION</div>

  <div class="btn" style="left:37px;top:67px;width:75px;height:58px">Reset<br>Hours</div>
  <div class="btn" style="left:37px;top:262px;width:75px;height:58px">Reset<br>Hours</div>
  <div class="btn" style="left:37px;top:467px;width:75px;height:58px">Reset<br>Hours</div>
  <div class="btn" style="left:37px;top:662px;width:75px;height:58px">Reset<br>Hours</div>
  <div class="readout" style="left:115px;top:67px;width:77px;height:18px">12345 hrs</div>
  <div class="readout" style="left:115px;top:302px;width:77px;height:18px">12345 hrs</div>
  <div class="readout" style="left:115px;top:468px;width:77px;height:18px">12345 hrs</div>
  <div class="readout" style="left:115px;top:702px;width:77px;height:18px">12345 hrs</div>

  <div class="btn" style="left:252px;top:165px;width:115px;height:58px">Change<br>Sea Water<br>Pump</div>
  <div class="btn btn-grey" style="left:57px;top:331px;width:193px;height:95px">SYSTEM ENABLE<br>SWITCH OFF</div>
  <div class="btn" style="left:270px;top:331px;width:97px;height:95px">Show<br>System<br>Config<br>Bottoms</div>
  <div class="btn" style="left:252px;top:565px;width:115px;height:58px">Change<br>Circulation<br>Pump</div>

  <div class="readout readout-lg" style="left:252px;top:28px;width:95px;height:38px">12.1°C</div>
  <div class="readout readout-lg" style="left:252px;top:262px;width:95px;height:38px">12.1°C</div>
  <div class="readout readout-lg" style="left:252px;top:662px;width:95px;height:38px">12.1°C</div>
  <div class="btn" style="left:192px;top:685px;width:56px;height:55px">–</div>
  <div class="readout readout-target" style="left:252px;top:703px;width:95px;height:37px">TARGET<br>12.1°C</div>
  <div class="btn" style="left:348px;top:685px;width:58px;height:55px">+</div>
  <div class="readout mode-display" style="left:408px;top:703px;width:428px;height:36px">SUMMER - COOLING MODE</div>
  <div class="btn" style="left:837px;top:686px;width:115px;height:53px">Change to<br>Heating Mode</div>

  <!-- chiller units -->
  <div class="chiller" style="left:525px;top:127px">
    <div class="chiller-temps"><span class="value">12.1 °C</span><span class="value">12.1 °C</span></div>
    <div class="chiller-alarms">
      <div class="alarm-row"><span class="box alarm-count">1</span><span class="alarm-tag">HP!!!</span><span class="box pressure">12.1</span><span class="unit">BAR</span></div>
      <div class="alarm-row"><span class="spacer"></span><span class="alarm-tag">LP!!!</span><span class="box pressure">12.1</span><span class="unit">BAR</span></div>
    </div>
    <div class="freeze-stop">FREEZE STOP</div>
    <div class="inhibit-toggle"><span>ENABLED</span><span>PRESS TO INHIBIT</span></div>
    <div class="chiller-name">CHILLER #1</div>
    <div class="run-hours"><span class="box">12345</span><span>hrs</span></div>
  </div>
  <div class="chiller" style="left:739px;top:127px">
    <div class="chiller-temps"><span class="value">12.1 °C</span><span class="value">12.1 °C</span></div>
    <div class="chiller-alarms">
      <div class="alarm-row"><span class="box alarm-count">1</span><span class="alarm-tag">HP!!!</span><span class="box pressure">12.1</span><span class="unit">BAR</span></div>
      <div class="alarm-row"><span class="spacer"></span><span class="alarm-tag">LP!!!</span><span class="box pressure">12.1</span><span class="unit">BAR</span></div>
    </div>
    <div class="freeze-stop">FREEZE STOP</div>
    <div class="inhibit-toggle"><span>ENABLED</span><span>PRESS TO INHIBIT</span></div>
    <div class="chiller-name">CHILLER #1</div>
    <div class="run-hours"><span class="box">12345</span><span>hrs</span></div>
  </div>
  <div class="chiller" style="left:953px;top:127px">
    <div class="chiller-temps"><span class="value">12.1 °C</span><span class="value">12.1 °C</span></div>
    <div class="chiller-alarms">
      <div class="alarm-row"><span class="box alarm-count">1</span><span class="alarm-tag">HP!!!</span><span class="box pressure">12.1</span><span class="unit">BAR</span></div>
      <div class="alarm-row"><span class="spacer"></span><span class="alarm-tag">LP!!!</span><span class="box pressure">12.1</span><span class="unit">BAR</span></div>
    </div>
    <div class="freeze-stop">FREEZE STOP</div>
    <div class="inhibit-toggle"><span>ENABLED</span><span>PRESS TO INHIBIT</span></div>
    <div class="chiller-name">CHILLER #1</div>
    <div class="run-hours"><span class="box">12345</span><span>hrs</span></div>
  </div>
  <div class="chiller" style="left:525px;top:459px">
    <div class="chiller-temps"><span class="value">12.1 °C</span><span class="value">12.1 °C</span></div>
    <div class="chiller-alarms">
      <div class="alarm-row"><span class="box alarm-count">1</span><span class="alarm-tag">HP!!!</span><span class="box pressure">12.1</span><span class="unit">BAR</span></div>
      <div class="alarm-row"><span class="spacer"></span><span class="alarm-tag">LP!!!</span><span class="box pressure">12.1</span><span class="unit">BAR</span></div>
    </div>
    <div class="freeze-stop">FREEZE STOP</div>
    <div class="inhibit-toggle"><span>ENABLED</span><span>PRESS TO INHIBIT</span></div>
    <div class="chiller-name">CHILLER #1</div>
    <div class="run-hours"><span class="box">12345</span><span>hrs</span></div>
  </div>
  <div class="chiller" style="left:739px;top:459px">
    <div class="chiller-temps"><span class="value">12.1 °C</span><span class="value">12.1 °C</span></div>
    <div class="chiller-alarms">
      <div class="alarm-row"><span class="box alarm-count">1</span><span class="alarm-tag">HP!!!</span><span class="box pressure">12.1</span><span class="unit">BAR</span></div>
      <div class="alarm-row"><span class="spacer"></span><span class="alarm-tag">LP!!!</span><span class="box pressure">12.1</span><span class="unit">BAR</span></div>
    </div>
    <div class="freeze-stop">FREEZE STOP</div>
    <div class="inhibit-toggle"><span>ENABLED</span><span>PRESS TO INHIBIT</span></div>
    <div class="chiller-name">CHILLER #1</div>
    <div class="run-hours"><span class="box">12345</span><span>hrs</span></div>
  </div>
  <div class="chiller" style="left:953px;top:459px">
    <div class="chiller-temps"><span class="value">12.1 °C</span><span class="value">12.1 °C</span></div>
    <div class="chiller-alarms">
      <div class="alarm-row"><span class="box alarm-count">1</span><span class="alarm-tag">HP!!!</span><span class="box pressure">12.1</span><span class="unit">BAR</span></div>
      <div class="alarm-row"><span class="spacer"></span><span class="alarm-tag">LP!!!</span><span class="box pressure">12.1</span><span class="unit">BAR</span></div>
    </div>
    <div class="freeze-stop">FREEZE STOP</div>
    <div class="inhibit-toggle"><span>ENABLED</span><span>PRESS TO INHIBIT</span></div>
    <div class="chiller-name">CHILLER #1</div>
    <div class="run-hours"><span class="box">12345</span><span>hrs</span></div>
  </div>
</div>
</body>
</html>
```